Business Card Design

We are a commercial real estate brokerage in San Francisco, leasing office buildings downtown.
I would like a clean, elegant look. Simple but powerful .

Industry/Entity Type

Business

Contact Information for Business Card

Colin Farrow
lic# 07281549
415.555.0172
colin@tarvo-commercial.example
tarvo-commercial.example

```html
<!DOCTYPE html>
<html lang="en">
<head>
<meta charset="utf-8">
<title>Tarvo Commercial — Business Card</title>
<link rel="stylesheet" href="https://fonts.googleapis.com/css2?family=Open+Sans:wght@400;600;700&display=swap">
<style>
  :root {
    --backdrop: #3b3431;
    --card: #131418;
    --brand: #8e9db6;
    --text: #8b9097;
    --text-strong: #9aa0a8;
    --rule: #3a3d44;
  }
  * { box-sizing: border-box; margin: 0; padding: 0; }
  html, body {
    width: 1200px; height: 768px; overflow: hidden;
    background: var(--backdrop);
    font-family: "Open Sans", Arial, sans-serif;
  }
  .stage {
    width: 1200px; height: 768px;
    display: flex; align-items: center; justify-content: center; gap: 48px;
  }
  .card {
    width: 525px; height: 300px;
    background: var(--card);
    position: relative;
    box-shadow: 0 10px 30px rgba(0,0,0,.45);
  }
  .brand {
    color: var(--brand);
    font-weight: 700;
    text-transform: uppercase;
    line-height: .95;
  }
  .brand-mark {
    width: 14px; height: 14px; background: var(--brand); display: inline-block;
  }
  /* front */
  .card-front { display: flex; align-items: center; justify-content: center; }
  .card-front .lockup { display: flex; align-items: center; gap: 18px; }
  .card-front .divider { width: 1px; height: 96px; background: var(--rule); }
  .card-front .brand-name { font-size: 56px; letter-spacing: 1px; }
  .card-front .brand-sub { font-size: 27px; letter-spacing: 1.5px; }
  /* back */
  .card-back .lockup {
    position: absolute; left: 40px; top: 92px; width: 180px;
    display: flex; flex-direction: column; align-items: flex-start; gap: 8px;
  }
  .card-back .lockup .rule { width: 160px; height: 2px; background: var(--rule); }
  .card-back .brand-name { font-size: 40px; letter-spacing: 1px; }
  .card-back .brand-sub { font-size: 19px; letter-spacing: 1px; }
  .contact { position: absolute; left: 270px; top: 96px; color: var(--text); }
  .contact .name { font-size: 20px; font-weight: 600; color: var(--text-strong); letter-spacing: .5px; }
  .contact .role { font-size: 11px; margin-top: 2px; margin-bottom: 22px; }
  .contact ul { list-style: none; font-size: 13px; line-height: 22px; }
  .contact li { display: flex; align-items: center; gap: 8px; }
  .contact svg { width: 12px; height: 12px; fill: var(--text); flex: none; }
</style>
</head>
<body>
<main class="stage">
  <section class="card card-front" aria-label="Card front">
    <div class="lockup">
      <span class="brand-mark"></span>
      <span class="divider"></span>
      <div class="brand">
        <div class="brand-name">Tarvo</div>
        <div class="brand-sub">Commercial</div>
      </div>
    </div>
  </section>

  <section class="card card-back" aria-label="Card back">
    <div class="lockup">
      <span class="brand-mark"></span>
      <div class="rule"></div>
      <div class="brand">
        <div class="brand-name">Tarvo</div>
        <div class="brand-sub">Commercial</div>
      </div>
    </div>
    <div class="contact">
      <div class="name">Colin Farrow</div>
      <div class="role">Managing Director</div>
      <ul>
        <li><svg viewBox="0 0 12 12" aria-hidden="true"><path d="M2.5 1h2l1 3-1.3 1a6 6 0 0 0 2.8 2.8L8 6.5l3 1v2A1.5 1.5 0 0 1 9.5 11 8.5 8.5 0 0 1 1 2.5 1.5 1.5 0 0 1 2.5 1z"/></svg>415.555.0172</li>
        <li><svg viewBox="0 0 12 12" aria-hidden="true"><path d="M1 2.5h10v7H1z M1.5 3l4.5 3.5L10.5 3" fill="none" stroke="#8b9097" stroke-width="1"/></svg>colin@tarvo-commercial.example</li>
        <li><svg viewBox="0 0 12 12" aria-hidden="true"><circle cx="6" cy="6" r="4.8" fill="none" stroke="#8b9097"/><path d="M1.2 6h9.6M6 1.2c-2.4 3-2.4 6.6 0 9.6M6 1.2c2.4 3 2.4 6.6 0 9.6" fill="none" stroke="#8b9097" stroke-width=".8"/></svg>www.tarvo-commercial.example</li>
        <li>LIC# 07281549</li>
      </ul>
    </div>
  </section>
</main>
</body>
</html>
```